Business Card Design

I am starting up a clothing business that designs and manufactures clothing for those with a disability in the younger age group of 16-28 years. My disabled daughter has finished school and as her mother I am aware of the difficulties in finding clothing to fit her. I am also aware of the difficulty for others of her age group regardless of gender who have difficulty dressing in clothes that suit their age because of their affliction.

I would like a card that has a design on the front referring to an unlimited sky and perhaps a rainbow or balloons indicating limitless possibilities. Within the rainbow of jewel colours (rather than typical red, yellow etc) I wish to contain words along the lines of ......For the young adult, Wheelchair bound, Restricted movement, Fumble free designs, On trend, Grace and dignity, Unique to your needs.

On the reverse or interior of a folding card I would like ......:-
Design & Manufacture of clothing for those with limited physical or cognitive ability at 47 Tallowmere Road, Wattlebrook, Qld, 4812

Name: …………………………………………………………….………
Your next appointment is ……..../……..../…….... at the time of …………………….. to be held at ……………………….
…………………………………………………………………………………

Target Market(s)

audience of any age, product targets 18-28 years age group with disabilties

Industry/Entity Type

Clothing

Contact Information for Business Card

MARIGOLD HARBOUR CLOTHING – 0412 596 201

PO Box 3152
Mount Pleasant Qld 4812

Requirements
Must have
• reference to a sky with some clouds, a rainbow or hot air balloons or some other item of many colours indicating the sky/possibilities are endless
Should not have
• people of obvious disabilities displayed

```html
<!DOCTYPE html>
<html lang="en">
<head>
<meta charset="utf-8">
<title>Appointment Card – Marigold Harbour Clothing</title>
<link rel="stylesheet" href="https://fonts.googleapis.com/css2?family=Jost:wght@600;700&display=swap">
<style>
  :root {
    --sky-cyan: #3ab4e6;
    --sky-deep: #1b6fb3;
    --sky-pale: #cdeaf7;
    --card-white: #ffffff;
    --card-edge: #f2b9bd;
    --mist: #e4e4e4;
    --band-violet: #6a1fd1;
    --band-indigo: #243fb0;
    --band-blue: #0060b8;
    --band-green: #22e022;
    --band-lime: #d8f000;
    --band-orange: #ff5a00;
    --band-red: #ff1020;
    --corner-rose: #f3b8b8;
    --corner-leaf: #dff3c4;
  }
  html, body {
    margin: 0;
    padding: 0;
    overflow: hidden;
    background: #ffffff;
  }
  .canvas {
    position: relative;
    width: 1200px;
    height: 725px;
    overflow: hidden;
    font-family: "Jost", "Futura", sans-serif;
  }
  .backdrop {
    position: absolute;
    inset: 0;
  }
  .card {
    position: absolute;
    left: 20px;
    top: 20px;
    width: 1158px;
    height: 683px;
    background: var(--card-white);
    border: 2px solid var(--card-edge);
    box-sizing: border-box;
  }
  .cloud-texture {
    position: absolute;
    inset: 0;
    background:
      radial-gradient(ellipse 260px 180px at 18% 30%, var(--mist), transparent 70%),
      radial-gradient(ellipse 300px 200px at 80% 25%, var(--mist), transparent 70%),
      radial-gradient(ellipse 340px 200px at 35% 85%, var(--mist), transparent 70%),
      radial-gradient(ellipse 280px 190px at 85% 80%, var(--mist), transparent 70%),
      radial-gradient(ellipse 260px 160px at 55% 55%, #efefef, transparent 70%);
  }
  .headline {
    position: absolute;
    left: 0;
    right: 0;
    top: 62px;
    margin: 0;
    text-align: center;
    color: var(--sky-cyan);
    font-weight: 700;
    font-size: 39px;
    line-height: 56px;
    letter-spacing: 3px;
    text-transform: uppercase;
    text-shadow: 0 0 6px #ffffff, 0 0 10px #ffffff;
  }
  .divider {
    position: absolute;
    left: 205px;
    top: 333px;
    width: 720px;
    height: 4px;
    border-radius: 2px;
    background: linear-gradient(90deg, transparent, var(--sky-pale) 20%, var(--sky-cyan) 50%, var(--sky-pale) 80%, transparent);
    filter: blur(0.6px);
  }
  .form {
    position: absolute;
    left: 114px;
    width: 912px;
    top: 377px;
    color: var(--sky-deep);
    font-weight: 700;
    font-size: 21px;
    letter-spacing: 2.4px;
    text-transform: uppercase;
  }
  .form-row {
    display: flex;
    align-items: flex-end;
    height: 26px;
    margin-bottom: 40px;
  }
  .label { white-space: nowrap; }
  .fill {
    flex: 1;
    border-bottom: 3px dotted var(--sky-deep);
    margin: 0 8px 5px;
    height: 0;
  }
  .fill.date { flex: 0 0 82px; margin: 0 2px 5px; }
  .fill.time { flex: 0 0 216px; margin: 0 12px 5px 0; }
  .fill.first { margin-left: 0; }
  .fill.last { margin-right: 0; }
</style>
</head>
<body>
<main class="canvas">
  <svg class="backdrop" width="1200" height="725" viewBox="0 0 1200 725" aria-hidden="true">
    <defs>
      <linearGradient id="sideSky" x1="0" y1="0" x2="0" y2="1">
        <stop offset="0" stop-color="#f0f6f8"/>
        <stop offset="0.4" stop-color="#5fd8ea"/>
        <stop offset="1" stop-color="#2aa6e3"/>
      </linearGradient>
    </defs>
    <rect width="1200" height="725" fill="#f4f7f8"/>
    <rect x="0" y="0" width="60" height="230" fill="var(--corner-rose)"/>
    <rect x="960" y="0" width="240" height="40" fill="var(--corner-leaf)"/>
    <rect x="0" y="240" width="24" height="485" fill="url(#sideSky)"/>
    <rect x="0" y="690" width="1200" height="35" fill="#7ec9ec"/>
    <g class="rainbow-left">
      <rect x="0" y="234" width="24" height="6" fill="var(--band-red)"/>
      <rect x="0" y="240" width="24" height="6" fill="var(--band-lime)"/>
      <rect x="0" y="246" width="24" height="6" fill="var(--band-green)"/>
      <rect x="0" y="252" width="24" height="8" fill="var(--band-blue)"/>
      <rect x="0" y="260" width="24" height="8" fill="var(--band-violet)"/>
      <rect x="0" y="268" width="24" height="10" fill="#ff4fb0"/>
    </g>
    <g class="rainbow-bottom" transform="skewX(-20)">
      <rect x="1060" y="700" width="48" height="25" fill="var(--band-violet)"/>
      <rect x="1108" y="700" width="48" height="25" fill="var(--band-indigo)"/>
      <rect x="1156" y="700" width="48" height="25" fill="var(--band-blue)"/>
      <rect x="1204" y="700" width="48" height="25" fill="var(--band-green)"/>
      <rect x="1252" y="700" width="48" height="25" fill="var(--band-lime)"/>
      <rect x="1300" y="700" width="48" height="25" fill="var(--band-orange)"/>
      <rect x="1348" y="700" width="60" height="25" fill="var(--band-red)"/>
    </g>
  </svg>

  <section class="card">
    <div class="cloud-texture" role="img" aria-label="Faint grey cloud splatter texture across the card background"></div>

    <h1 class="headline">Design &amp; Manufacture of clothing<br>for those with limited physical or<br>cognitive ability at 47 Tallowmere<br>Road, Wattlebrook, Qld, 4812</h1>

    <div class="divider"></div>

    <div class="form">
      <div class="form-row">
        <span class="label">Name:</span><span class="fill last"></span>
      </div>
      <div class="form-row">
        <span class="label">Your next appointment is</span>
        <span class="fill date"></span><span class="label">/</span>
        <span class="fill date"></span><span class="label">/</span>
        <span class="fill date"></span>
        <span class="label">&nbsp;at the time of</span>
      </div>
      <div class="form-row">
        <span class="fill time first"></span>
        <span class="label">to be held at</span><span class="fill last"></span>
      </div>
      <div class="form-row">
        <span class="fill first last"></span>
      </div>
    </div>
  </section>
</main>
</body>
</html>
```